Webdesign für IT-Dienstleister
Zielgruppe
Seit 1997 bieten wir erstklassige IT-Dienstleistungen Mainz an, die darauf ausgerichtet sind, Unternehmen und Privatkunden mit kompetenter Beratung, zuverlässiger Unterstützung und modernen Technologielösungen zur Seite zu stehen.
Umfassende Computer-Serviceleistungen
Unser Computer-Service Mainz beinhaltet eine Reihe von Dienstleistungen, die darauf abzielen, die Leistungsfähigkeit Ihrer IT-Infrastruktur zu optimieren und zu erhalten. Von der Fehlerdiagnose bis hin zur Wartung bieten wir ein Rundum-Sorglos-Paket für Ihre Hardware und Software.
Professionelle Fehleranalyse und Reparatur
Optimierung von Betriebssystemen und Anwendungen
Regelmäßige Wartungsarbeiten zur Vorbeugung von Ausfällen
Ersetzen und Aufrüsten von Hardware-Komponenten
Aufgabenstellung
Ich hätte gern ein modernes Design. Ein Logo vorhanden, sollte mit eingebaut werden.
Ansonsten hätte ich gerne eine einzelne Webseite mit den Firmen Infos (und den Links zu Sozial Media) und einer extra Impressum Seite. Und wenn möglich noch ein Anfrage Formular.
Am liebsten wäre ein Format welches ich in WordPress verarbeiten werden kann.
(Logo wird noch nachgereicht)

```html
<!DOCTYPE html>
<html lang="de">
<head>
<meta charset="utf-8">
<title>rechnerwerk-halvo.de – IT-Services</title>
<link href="https://fonts.googleapis.com/css2?family=Poppins:wght@400;500;600;700&display=swap" rel="stylesheet">
<style>
:root{
  --cyan:#29b3e0;
  --cyan-soft:#e6f6fc;
  --navy:#1f2b57;
  --ink:#161b33;
  --text:#4d5570;
  --muted:#7a8199;
  --line:#dfe3ea;
  --bg-soft:#f5f6f9;
  --footer:#111631;
}
*{box-sizing:border-box;margin:0;padding:0}
html,body{width:1200px;height:5036px;overflow:hidden}
body{font-family:"Poppins",sans-serif;color:var(--ink);background:#fff}
.wrap{width:1052px;margin:0 auto}
svg{display:block}

/* top bar */
.topbar{height:29px;background:var(--cyan);color:#fff;font-size:11px}
.topbar .wrap{display:flex;justify-content:space-between;align-items:center;height:29px}
.topbar .contacts{display:flex;gap:20px}
.topbar .contacts span,.topbar .social{display:flex;align-items:center;gap:6px}
.topbar .social{gap:18px}
.dot{width:8px;height:8px;border-radius:50%;background:#fff;opacity:.85}

/* nav */
.nav{height:55px;border-bottom:1px solid var(--line)}
.nav .wrap{display:flex;align-items:center;justify-content:space-between;height:55px}
.brand{display:flex;align-items:center;gap:8px}
.brand-mark{width:30px;height:30px;border-radius:50%;background:var(--navy)}
.brand-name{font-weight:600;font-size:16px;color:var(--navy)}
.menu{display:flex;align-items:center;gap:28px;font-size:13px;font-weight:500}
.btn-fill{background:var(--cyan);color:#fff;font-weight:600;font-size:14px;padding:9px 22px;border-radius:6px}

/* hero */
.hero{position:relative;height:336px;color:#fff;text-align:center;overflow:hidden}
.hero-bg{position:absolute;inset:0;background:linear-gradient(180deg,#2a3a72 0%,#3b4f8e 55%,#2c3d78 100%)}
.hero-inner{position:relative;padding-top:60px}
.hero h1{font-size:42px;font-weight:700;line-height:1.2}
.hero p{width:620px;margin:18px auto 0;font-size:16px;line-height:23px}
.hero .btn-fill{display:inline-block;margin-top:28px;font-size:13px;padding:12px 26px}

/* services */
.services{height:2960px;padding-top:70px}
.section-head{text-align:center}
.section-head h2{font-size:33px;font-weight:700;line-height:1.25}
.section-head p{width:560px;margin:14px auto 0;font-size:16px;line-height:24px;color:var(--text)}
.rows{margin-top:41px;display:flex;flex-direction:column;gap:56px}
.row{display:grid;grid-template-columns:505px 505px;column-gap:42px;align-items:center;height:400px}
.row.flip .media{order:-1}
.icon-box{width:44px;height:44px;border-radius:10px;background:var(--cyan-soft);display:flex;align-items:center;justify-content:center}
.row h3{font-size:25px;font-weight:700;margin-top:22px}
.row .lead{margin-top:14px;font-size:15px;line-height:24px;color:var(--text)}
.checks{list-style:none;margin-top:18px;display:flex;flex-direction:column;gap:14px}
.checks li{display:grid;grid-template-columns:16px 1fr;column-gap:14px}
.checks svg{margin-top:4px}
.checks b{font-size:13px;font-weight:600;display:block}
.checks small{font-size:11px;color:var(--muted);display:block;margin-top:2px}
.btn-line{display:inline-block;margin-top:28px;border:2px solid var(--navy);color:var(--navy);border-radius:6px;font-size:13px;font-weight:600;padding:10px 20px}
.media{height:323px;border-radius:12px;box-shadow:0 10px 24px rgba(20,30,60,.18)}
.m-dev{background:linear-gradient(135deg,#e9ebee,#c9cdd3)}
.m-acc{background:linear-gradient(135deg,#dfe6ee,#a9b6c4)}
.m-rep{background:linear-gradient(135deg,#cfd6de,#3a4250)}
.m-net{background:linear-gradient(135deg,#1a2436,#2d5fb0)}
.m-svc{background:linear-gradient(135deg,#e2e6ec,#5b6472)}
.m-dsl{background:linear-gradient(135deg,#c7d2de,#e9eef3)}

/* why */
.why{height:432px;padding-top:74px}
.why .section-head p{margin-top:8px;font-size:16px}
.features{margin-top:45px;display:grid;grid-template-columns:repeat(4,1fr);gap:30px;text-align:center}
.feature .icon-box{margin:0 auto}
.feature h4{margin-top:26px;font-size:16px;font-weight:600}
.feature p{margin-top:10px;font-size:13px;line-height:20px;color:var(--text)}

/* contact */
.contact{height:841px;background:var(--bg-soft);padding-top:70px}
.contact .section-head p{margin-top:6px;font-size:16px}
.contact-grid{margin-top:48px;display:grid;grid-template-columns:506px 506px;column-gap:40px}
.contact-info h3{font-size:19px;font-weight:600;margin-top:12px}
.info-list{margin-top:26px;display:flex;flex-direction:column;gap:26px}
.info-item{display:grid;grid-template-columns:38px 1fr;column-gap:18px}
.info-icon{width:38px;height:38px;border-radius:50%;background:var(--cyan-soft);display:flex;align-items:center;justify-content:center}
.info-item b{font-size:13px;font-weight:600;display:block;margin-bottom:4px}
.info-item span{display:block;font-size:13px;line-height:20px;color:var(--text)}
.form-card{background:#fff;border-radius:12px;padding:28px 26px;box-shadow:0 4px 16px rgba(20,30,60,.06);height:576px}
.form-card h3{font-size:19px;font-weight:600}
.fields{margin-top:20px;display:grid;grid-template-columns:1fr 1fr;column-gap:14px;row-gap:16px}
.field label{display:block;font-size:11px;font-weight:500;margin-bottom:6px}
.input{height:36px;border:1px solid var(--line);border-radius:8px;background:#fff}
.select{display:flex;align-items:center;justify-content:space-between;padding:0 12px;font-size:12px}
.full{grid-column:1/3}
.radios{display:flex;gap:22px;font-size:12px;color:var(--text)}
.radios span{display:flex;align-items:center;gap:6px}
.radio{width:13px;height:13px;border-radius:50%;border:1px solid #9aa0b0}
.radio.on{border:4px solid var(--navy)}
.textarea{height:108px;border:1px solid var(--line);border-radius:8px;padding:10px 14px;font-size:11px;color:var(--muted)}
.consent{display:flex;gap:12px;font-size:11px;line-height:16px;color:var(--text);margin-top:6px}
.box{width:13px;height:13px;border:1px solid #9aa0b0;border-radius:3px;flex:none;margin-top:2px}
.submit{margin-top:18px;height:40px;border-radius:6px;background:var(--navy);color:#fff;font-size:13px;font-weight:600;display:flex;align-items:center;justify-content:center}

/* footer */
.footer{height:383px;background:var(--footer);color:#c3c8d8;padding-top:50px;position:relative}
.footer-grid{display:grid;grid-template-columns:360px 360px 1fr;font-size:13px}
.footer .brand-name{color:#fff}
.footer .brand-mark{background:var(--cyan)}
.footer-about{margin-top:22px;line-height:21px;width:300px}
.footer-social{display:flex;gap:12px;margin-top:22px}
.footer-social span{width:26px;height:26px;border-radius:50%;background:#222946}
.footer h5{color:#fff;font-size:14px;font-weight:600;margin-top:4px}
.f-list{margin-top:22px;display:flex;flex-direction:column;gap:12px;line-height:20px}
.f-list li{list-style:none;display:flex;gap:10px}
.copy{position:absolute;left:0;right:0;bottom:46px;text-align:center;font-size:12px;border-top:1px solid #232a48;padding-top:30px;width:1052px;margin:0 auto}
</style>
</head>
<body>

<div class="topbar">
  <div class="wrap">
    <div class="contacts">
      <span><svg width="11" height="11" viewBox="0 0 24 24" fill="none" stroke="#fff" stroke-width="2"><path d="M5 3h4l2 5-3 2a12 12 0 0 0 6 6l2-3 5 2v4a2 2 0 0 1-2 2A18 18 0 0 1 3 5a2 2 0 0 1 2-2z"/></svg>+49 6131 480270</span>
      <span><svg width="12" height="11" viewBox="0 0 24 24" fill="none" stroke="#fff" stroke-width="2"><rect x="3" y="5" width="18" height="14" rx="2"/><path d="M3 7l9 6 9-6"/></svg>info@nervak.eu</span>
    </div>
    <div class="social"><i class="dot"></i><i class="dot"></i><i class="dot"></i></div>
  </div>
</div>

<header class="nav">
  <div class="wrap">
    <div class="brand"><span class="brand-mark"></span><span class="brand-name">rechnerwerk-halvo.de</span></div>
    <nav class="menu"><span>Home</span><span>Services</span><span>Verkauf</span><span>Kontakt</span><span class="btn-fill">Service anfordern</span></nav>
  </div>
</header>

<section class="hero">
  <div class="hero-bg" role="img" aria-label="Foto eines modernen Büros mit Bildschirmarbeitsplätzen in blauem Licht"></div>
  <div class="hero-inner">
    <h1>Unsere IT-Services</h1>
    <p>Professionelle IT-Dienstleistungen für Unternehmen und Privatkunden in Mainz. Von der Fehleranalyse bis zur kompletten Systemoptimierung – wir sind Ihr zuverlässiger Partner.</p>
    <span class="btn-fill">Service anfragen</span>
  </div>
</section>

<section class="services">
  <div class="wrap">
    <div class="section-head">
      <h2>Detaillierte Service-Übersicht</h2>
      <p>Entdecken Sie unser umfassendes Portfolio an IT-Dienstleistungen, maßgeschneidert für Ihre individuellen Anforderungen.</p>
    </div>

    <div class="rows">
      <div class="row">
        <div>
          <div class="icon-box"><svg width="20" height="20" viewBox="0 0 24 24" fill="none" stroke="#29b3e0" stroke-width="1.8"><rect x="3" y="4" width="18" height="16" rx="2"/><path d="M9 10l-2 2 2 2M15 10l2 2-2 2"/></svg></div>
          <h3>Softwareentwicklung &amp; Anpassungen</h3>
          <p class="lead">Unsere Entwickler realisieren maßgeschneiderte Anwendungen, Integrationen und Automatisierungen – skalierbar, sicher und exakt auf Ihre Prozesse abgestimmt.</p>
          <ul class="checks">
            <li><svg width="14" height="14" viewBox="0 0 24 24" fill="none" stroke="#29b3e0" stroke-width="2.5"><path d="M4 12l5 5L20 6"/></svg><div><b>Individuelle Anwendungen</b><small>Web- und Desktop-Software exakt nach Anforderung, inkl. UI/UX-Konzeption.</small></div></li>
            <li><svg width="14" height="14" viewBox="0 0 24 24" fill="none" stroke="#29b3e0" stroke-width="2.5"><path d="M4 12l5 5L20 6"/></svg><div><b>Schnittstellen &amp; Automatisierung</b><small>API-Anbindungen, Datenimporte/-Exporte und Workflow-Automatisierung.</small></div></li>
            <li><svg width="14" height="14" viewBox="0 0 24 24" fill="none" stroke="#29b3e0" stroke-width="2.5"><path d="M4 12l5 5L20 6"/></svg><div><b>Wartung &amp; Weiterentwicklung</b><small>Regelmäßige Updates, Bugfixes und Performance-Optimierungen.</small></div></li>
          </ul>
          <span class="btn-line">Service anfragen</span>
        </div>
        <div class="media m-dev" role="img" aria-label="Foto eines Laptops mit Programmcode auf einem Schreibtisch mit Lampe und Tasse"></div>
      </div>

      <div class="row flip">
        <div>
          <div class="icon-box"><svg width="20" height="20" viewBox="0 0 24 24" fill="none" stroke="#29b3e0" stroke-width="1.8"><rect x="5" y="4" width="14" height="16" rx="2"/><path d="M9 9h6v4H9z"/></svg></div>
          <h3>Computerzubehör &amp; Beratung</h3>
          <p class="lead">Umfangreiches Sortiment an Zubehör – Tastaturen, Headsets, Drucker, Router u.v.m. Mit persönlicher Beratung im Mainzer Shop.</p>
          <ul class="checks">
            <li><svg width="14" height="14" viewBox="0 0 24 24" fill="none" stroke="#29b3e0" stroke-width="2.5"><path d="M4 12l5 5L20 6"/></svg><div><b>Große Auswahl</b><small>Peripherie &amp; Zubehör führender Marken sofort verfügbar.</small></div></li>
            <li><svg width="14" height="14" viewBox="0 0 24 24" fill="none" stroke="#29b3e0" stroke-width="2.5"><path d="M4 12l5 5L20 6"/></svg><div><b>Kompatibilitäts-Beratung</b><small>Wir prüfen, was zu Ihrem System passt – stressfrei einkaufen.</small></div></li>
            <li><svg width="14" height="14" viewBox="0 0 24 24" fill="none" stroke="#29b3e0" stroke-width="2.5"><path d="M4 12l5 5L20 6"/></svg><div><b>Einrichtung &amp; Support</b><small>Vor-Ort-Installation, Treiber &amp; Firmware – alles aus einer Hand.</small></div></li>
          </ul>
          <span class="btn-line">Service anfragen</span>
        </div>
        <div class="media m-acc" role="img" aria-label="Foto von Tastatur, Maus, Headset und USB-Stick auf hellem Tisch"></div>
      </div>

      <div class="row">
        <div>
          <div class="icon-box"><svg width="20" height="20" viewBox="0 0 24 24" fill="none" stroke="#29b3e0" stroke-width="1.8"><path d="M5 19l7-7M14 4l6 6-3 1-4-4zM4 4l4 4M8 4L4 8M15 15l4 4"/></svg></div>
          <h3>Fehlerdiagnose &amp; Reparatur</h3>
          <p class="lead">Gründliche Diagnose Ihrer Geräte, transparente Kostenvoranschläge und schnelle Reparatur – in der Werkstatt oder bei Ihnen vor Ort.</p>
          <ul class="checks">
            <li><svg width="14" height="14" viewBox="0 0 24 24" fill="none" stroke="#29b3e0" stroke-width="2.5"><path d="M4 12l5 5L20 6"/></svg><div><b>Hardware-/Software-Analyse</b><small>Fehlererkennung mit professionellen Test- und Diagnose-Tools.</small></div></li>
            <li><svg width="14" height="14" viewBox="0 0 24 24" fill="none" stroke="#29b3e0" stroke-width="2.5"><path d="M4 12l5 5L20 6"/></svg><div><b>Datenrettung</b><small>Rettung wichtiger Dateien von defekten Datenträgern.</small></div></li>
            <li><svg width="14" height="14" viewBox="0 0 24 24" fill="none" stroke="#29b3e0" stroke-width="2.5"><path d="M4 12l5 5L20 6"/></svg><div><b>Express-Service</b><small>Schnelle Reparaturen nach Verfügbarkeit – transparent &amp; zuverlässig.</small></div></li>
          </ul>
          <span class="btn-line">Service anfragen</span>
        </div>
        <div class="media m-rep" role="img" aria-label="Foto von Händen, die an einer Hauptplatine mit Festplatten arbeiten"></div>
      </div>

      <div class="row flip">
        <div>
          <div class="icon-box"><svg width="20" height="20" viewBox="0 0 24 24" fill="none" stroke="#29b3e0" stroke-width="1.8"><path d="M5 10a10 10 0 0 1 14 0M8 13a6 6 0 0 1 8 0"/><rect x="6" y="16" width="12" height="4" rx="1"/></svg></div>
          <h3>Computernetzwerk-Dienstleistungen</h3>
          <p class="lead">Planung, Aufbau und Absicherung leistungsfähiger Netzwerke für Büro, Home-Office und Filialen.</p>
          <ul class="checks">
            <li><svg width="14" height="14" viewBox="0 0 24 24" fill="none" stroke="#29b3e0" stroke-width="2.5"><path d="M4 12l5 5L20 6"/></svg><div><b>LAN/WLAN-Planung</b><small>Ausleuchtung, Kapazitätsplanung und saubere Dokumentation.</small></div></li>
            <li><svg width="14" height="14" viewBox="0 0 24 24" fill="none" stroke="#29b3e0" stroke-width="2.5"><path d="M4 12l5 5L20 6"/></svg><div><b>Firewall &amp; VPN</b><small>Sichere Standort- und Remote-Anbindungen mit Best-Practices.</small></div></li>
            <li><svg width="14" height="14" viewBox="0 0 24 24" fill="none" stroke="#29b3e0" stroke-width="2.5"><path d="M4 12l5 5L20 6"/></svg><div><b>Monitoring</b><small>Überwachung &amp; Performance-Tuning für hohe Verfügbarkeit.</small></div></li>
          </ul>
          <span class="btn-line">Service anfragen</span>
        </div>
        <div class="media m-net" role="img" aria-label="Foto eines Serverraums mit verkabelten Racks in blauem Licht"></div>
      </div>

      <div class="row">
        <div>
          <div class="icon-box"><svg width="20" height="20" viewBox="0 0 24 24" fill="none" stroke="#29b3e0" stroke-width="1.8"><rect x="4" y="5" width="16" height="15" rx="2"/><path d="M4 10h16M9 3v4M15 3v4"/></svg></div>
          <h3>Service &amp; Wartungsverträge</h3>
          <p class="lead">Planbare IT-Kosten, feste SLAs und proaktive Betreuung – wir halten Ihre Systeme zuverlässig am Laufen.</p>
          <ul class="checks">
            <li><svg width="14" height="14" viewBox="0 0 24 24" fill="none" stroke="#29b3e0" stroke-width="2.5"><path d="M4 12l5 5L20 6"/></svg><div><b>Proaktives Monitoring</b><small>Früherkennung von Problemen und automatisierte Wartungsaufgaben.</small></div></li>
            <li><svg width="14" height="14" viewBox="0 0 24 24" fill="none" stroke="#29b3e0" stroke-width="2.5"><path d="M4 12l5 5L20 6"/></svg><div><b>SLA-Reaktionszeiten</b><small>Garantierte Erreichbarkeit und definierte Lösungszeiten.</small></div></li>
            <li><svg width="14" height="14" viewBox="0 0 24 24" fill="none" stroke="#29b3e0" stroke-width="2.5"><path d="M4 12l5 5L20 6"/></svg><div><b>Regelmäßige Health-Checks</b><small>Planmäßige Systemprüfungen und Reportings.</small></div></li>
          </ul>
          <span class="btn-line">Service anfragen</span>
        </div>
        <div class="media m-svc" role="img" aria-label="Foto eines geöffneten Laptops, an dem mit Werkzeug gearbeitet wird"></div>
      </div>

      <div class="row flip">
        <div>
          <div class="icon-box"><svg width="20" height="20" viewBox="0 0 24 24" fill="none" stroke="#29b3e0" stroke-width="1.8"><path d="M3 9a13 13 0 0 1 18 0M6 12.5a8 8 0 0 1 12 0M9 16a4 4 0 0 1 6 0"/><circle cx="12" cy="19" r="1"/></svg></div>
          <h3>DSL &amp; Internet Produkte</h3>
          <p class="lead">Passende Internetlösungen für Privat- und Geschäftskunden – DSL/VDSL-Tarife, Router &amp; Mesh-WLAN, Einrichtung und Support.</p>
          <ul class="checks">
            <li><svg width="14" height="14" viewBox="0 0 24 24" fill="none" stroke="#29b3e0" stroke-width="2.5"><path d="M4 12l5 5L20 6"/></svg><div><b>Tarifberatung</b><small>DSL/VDSL-Angebote vergleichen und optimal auswählen.</small></div></li>
            <li><svg width="14" height="14" viewBox="0 0 24 24" fill="none" stroke="#29b3e0" stroke-width="2.5"><path d="M4 12l5 5L20 6"/></svg><div><b>Router &amp; Mesh-WLAN</b><small>Geräteauswahl, Einrichtung und Optimierung der Abdeckung.</small></div></li>
            <li><svg width="14" height="14" viewBox="0 0 24 24" fill="none" stroke="#29b3e0" stroke-width="2.5"><path d="M4 12l5 5L20 6"/></svg><div><b>Einrichtung &amp; Support</b><small>Vor-Ort-Installation, Störungsanalyse und laufender Support.</small></div></li>
          </ul>
          <span class="btn-line">Service anfragen</span>
        </div>
        <div class="media m-dsl" role="img" aria-label="Foto eines WLAN-Routers mit leuchtendem Funksymbol in einem hellen Raum"></div>
      </div>
    </div>
  </div>
</section>

<section class="why">
  <div class="wrap">
    <div class="section-head">
      <h2>Warum nervak.eu?</h2>
      <p>Über 25 Jahre Erfahrung sprechen für sich</p>
    </div>
    <div class="features">
      <div class="feature">
        <div class="icon-box"><svg width="20" height="20" viewBox="0 0 24 24" fill="none" stroke="#29b3e0" stroke-width="1.8"><circle cx="12" cy="9" r="5"/><path d="M9 13l-1 8 4-2 4 2-1-8"/></svg></div>
        <h4>25+ Jahre Erfahrung</h4>
        <p>Seit 1997 vertrauen Kunden in Mainz auf unsere Expertise und zuverlässigen Service.</p>
      </div>
      <div class="feature">
        <div class="icon-box"><svg width="20" height="20" viewBox="0 0 24 24" fill="none" stroke="#29b3e0" stroke-width="1.8"><circle cx="12" cy="7" r="3"/><circle cx="5" cy="10" r="2"/><circle cx="19" cy="10" r="2"/><path d="M7 20a5 5 0 0 1 10 0M2 19a3 3 0 0 1 5-2M22 19a3 3 0 0 0-5-2"/></svg></div>
        <h4>Zertifizierte Experten</h4>
        <p>Unser Team besteht aus zertifizierten IT-Spezialisten mit kontinuierlicher Weiterbildung.</p>
      </div>
      <div class="feature">
        <div class="icon-box"><svg width="20" height="20" viewBox="0 0 24 24" fill="none" stroke="#29b3e0" stroke-width="1.8"><circle cx="12" cy="12" r="8"/><path d="M12 8v4l3 2"/></svg></div>
        <h4>Schnelle Reaktion</h4>
        <p>Bei Notfällen sind wir innerhalb von 2 Stunden vor Ort – 24/7 Bereitschaft.</p>
      </div>
      <div class="feature">
        <div class="icon-box"><svg width="20" height="20" viewBox="0 0 24 24" fill="none" stroke="#29b3e0" stroke-width="1.8"><path d="M12 3l7 3v6c0 4-3 7-7 9-4-2-7-5-7-9V6z"/><path d="M9 12l2 2 4-4"/></svg></div>
        <h4>Garantie &amp; Sicherheit</h4>
        <p>Alle Arbeiten mit Garantie und höchsten Sicherheitsstandards für Ihre Daten.</p>
      </div>
    </div>
  </div>
</section>

<section class="contact">
  <div class="wrap">
    <div class="section-head">
      <h2>Service anfragen</h2>
      <p>Kontaktieren Sie uns für eine kostenlose Erstberatung</p>
    </div>
    <div class="contact-grid">
      <div class="contact-info">
        <h3>Kontaktinformationen</h3>
        <div class="info-list">
          <div class="info-item">
            <div class="info-icon"><svg width="16" height="16" viewBox="0 0 24 24" fill="none" stroke="#29b3e0" stroke-width="2"><path d="M12 21s-7-6-7-11a7 7 0 0 1 14 0c0 5-7 11-7 11z"/><circle cx="12" cy="10" r="2.5"/></svg></div>
            <div><b>Adresse</b><span>Lindenweg 14</span><span>55116 Mainz</span><span>Deutschland</span></div>
          </div>
          <div class="info-item">
            <div class="info-icon"><svg width="16" height="16" viewBox="0 0 24 24" fill="none" stroke="#29b3e0" stroke-width="2"><path d="M5 3h4l2 5-3 2a12 12 0 0 0 6 6l2-3 5 2v4a2 2 0 0 1-2 2A18 18 0 0 1 3 5a2 2 0 0 1 2-2z"/></svg></div>
            <div><b>Telefon</b><span>+49 6131 480270</span><span>Notfall-Hotline: +49 6131 480279</span></div>
          </div>
          <div class="info-item">
            <div class="info-icon"><svg width="16" height="16" viewBox="0 0 24 24" fill="none" stroke="#29b3e0" stroke-width="2"><rect x="3" y="5" width="18" height="14" rx="2"/><path d="M3 7l9 6 9-6"/></svg></div>
            <div><b>E-Mail</b><span>info@nervak.eu</span><span>service@nervak.eu</span></div>
          </div>
          <div class="info-item">
            <div class="info-icon"><svg width="16" height="16" viewBox="0 0 24 24" fill="none" stroke="#29b3e0" stroke-width="2"><circle cx="12" cy="12" r="8"/><path d="M12 8v4l3 2"/></svg></div>
            <div><b>Service-Zeiten</b><span>Mo-Fr: 08:00 - 18:00 Uhr</span><span>Sa: 09:00 - 14:00 Uhr</span><span>Notfall: 24/7 verfügbar</span></div>
          </div>
        </div>
      </div>

      <div class="form-card">
        <h3>Service-Anfrage</h3>
        <div class="fields">
          <div class="field"><label>Name *</label><div class="input"></div></div>
          <div class="field"><label>E-Mail *</label><div class="input"></div></div>
          <div class="field"><label>Telefon</label><div class="input"></div></div>
          <div class="field"><label>Service-Art *</label><div class="input select"><span>Service auswählen</span><svg width="10" height="10" viewBox="0 0 24 24" fill="none" stroke="#161b33" stroke-width="2.5"><path d="M6 9l6 6 6-6"/></svg></div></div>
          <div class="field full"><label>Dringlichkeit</label>
            <div class="radios"><span><i class="radio on"></i>Normal</span><span><i class="radio"></i>Dringend</span><span><i class="radio"></i>Notfall</span></div>
          </div>
          <div class="field full"><label>Problembeschreibung *</label><div class="textarea">Beschreiben Sie Ihr Problem oder Ihren Service-Wunsch...</div></div>
          <div class="full consent"><i class="box"></i><span>Ich stimme der Verarbeitung meiner Daten gemäß der Datenschutzerklärung zu. *</span></div>
        </div>
        <div class="submit">Service-Anfrage senden</div>
      </div>
    </div>
  </div>
</section>

<footer class="footer">
  <div class="wrap footer-grid">
    <div>
      <div class="brand"><span class="brand-mark"></span><span class="brand-name">rechnerwerk-halvo.de</span></div>
      <p class="footer-about">Seit 1997 Ihr vertrauensvoller Partner für professionelle IT-Dienstleistungen in Mainz.</p>
      <div class="footer-social"><span></span><span></span><span></span></div>
    </div>
    <div>
      <h5>Kontakt</h5>
      <ul class="f-list">
        <li><svg width="13" height="13" viewBox="0 0 24 24" fill="none" stroke="#c3c8d8" stroke-width="2"><path d="M12 21s-7-6-7-11a7 7 0 0 1 14 0c0 5-7 11-7 11z"/></svg><span>Lindenweg 14<br>55116 Mainz, Deutschland</span></li>
        <li><svg width="13" height="13" viewBox="0 0 24 24" fill="none" stroke="#c3c8d8" stroke-width="2"><path d="M5 3h4l2 5-3 2a12 12 0 0 0 6 6l2-3 5 2v4a2 2 0 0 1-2 2A18 18 0 0 1 3 5a2 2 0 0 1 2-2z"/></svg><span>+49 6131 480270</span></li>
        <li><svg width="13" height="13" viewBox="0 0 24 24" fill="none" stroke="#c3c8d8" stroke-width="2"><rect x="3" y="5" width="18" height="14" rx="2"/><path d="M3 7l9 6 9-6"/></svg><span>info@nervak.eu</span></li>
      </ul>
    </div>
    <div>
      <h5>Wichtige Links</h5>
      <ul class="f-list">
        <li>Home</li><li>Services</li><li>Kontakt</li><li>Impressum</li><li>Datenschutz</li>
      </ul>
    </div>
  </div>
  <div class="copy">© 2025 nervak.eu - IT-Dienstleistungen Halvo. Alle Rechte vorbehalten.</div>
</footer>

</body>
</html>
```